Business Cards for a law firm

Business cards for our law firm. Use our silhoette logo and OAK HARBOR - check our website (www.oakharbor-legal.com)

Contact Information for Business Card

our silhouette logo, OAK HARBOR, 800-555-0147, Dorian Kestrup, dorian@oakharbor-legal.com

Requirements
Must have
• our silhouette logo, OAK HARBOR, 800-555-0147, Dorian Kestrup, dorian@oakharbor-legal.com

```html
<!DOCTYPE html>
<html lang="en">
<head>
<meta charset="utf-8">
<title>Oak Harbor – Business Card</title>
<link rel="stylesheet" href="https://fonts.googleapis.com/css2?family=Cinzel:wght@600&family=Raleway:wght@300;400&display=swap">
<style>
  :root {
    --page-bg: #e4e4e5;
    --card-blue: #2f539a;
    --card-blue-deep: #26468a;
    --card-blue-light: #3d66a8;
    --accent-yellow: #ffcc00;
    --band-white: #ffffff;
    --ink-navy: #1f2d5c;
    --text-white: #ffffff;
  }
  * { margin: 0; padding: 0; box-sizing: border-box; }
  html, body {
    width: 1200px;
    height: 1100px;
    overflow: hidden;
    background: var(--page-bg);
  }
  .business-card {
    position: absolute;
    left: 198px;
    top: 310px;
    width: 775px;
    height: 446px;
    overflow: hidden;
    background: var(--card-blue);
  }
  .skyline-photo {
    position: absolute;
    inset: 0 0 56px 0;
    background:
      linear-gradient(115deg, rgba(255,255,255,0.06) 0%, rgba(255,255,255,0) 35%),
      linear-gradient(180deg, var(--card-blue-light) 0%, var(--card-blue) 45%, var(--card-blue-deep) 100%);
  }
  .holder-name {
    position: absolute;
    right: 84px;
    top: 42px;
    font-family: "Raleway", sans-serif;
    font-weight: 300;
    font-size: 25px;
    color: var(--text-white);
    letter-spacing: 0.3px;
  }
  .firm-mark {
    position: absolute;
    left: 86px;
    top: 164px;
    display: flex;
    align-items: center;
    gap: 40px;
  }
  .firm-mark-dot {
    width: 70px;
    height: 70px;
    border-radius: 50%;
    background: var(--text-white);
  }
  .firm-name {
    font-family: "Cinzel", serif;
    font-weight: 600;
    font-size: 46px;
    letter-spacing: 4px;
    color: var(--text-white);
    line-height: 1;
  }
  .contact-band {
    position: absolute;
    left: 0;
    bottom: 0;
    width: 100%;
    height: 56px;
    display: flex;
  }
  .contact-item {
    display: flex;
    align-items: center;
    justify-content: center;
    gap: 8px;
    height: 100%;
    font-family: "Raleway", sans-serif;
    font-weight: 400;
    font-size: 18px;
    color: var(--ink-navy);
    white-space: nowrap;
  }
  .contact-item svg { flex: none; fill: var(--ink-navy); }
  .contact-phone { width: 180px; background: var(--accent-yellow); }
  .contact-email { width: 310px; background: var(--band-white); }
  .contact-web { width: 285px; background: var(--accent-yellow); }
</style>
</head>
<body>
  <div class="business-card">
    <div class="skyline-photo" role="img" aria-label="Upward view of glass office towers in blue tones"></div>

    <p class="holder-name">Dorian Kestrup</p>

    <div class="firm-mark">
      <span class="firm-mark-dot"></span>
      <span class="firm-name">OAK HARBOR</span>
    </div>

    <div class="contact-band">
      <div class="contact-item contact-phone">
        <svg width="18" height="18" viewBox="0 0 24 24" aria-hidden="true">
          <path d="M6.6 10.8a15.1 15.1 0 0 0 6.6 6.6l2.2-2.2a1 1 0 0 1 1-.25 11.4 11.4 0 0 0 3.6.57 1 1 0 0 1 1 1V20a1 1 0 0 1-1 1A17 17 0 0 1 3 4a1 1 0 0 1 1-1h3.5a1 1 0 0 1 1 1c0 1.25.2 2.45.57 3.57a1 1 0 0 1-.25 1z"/>
        </svg>
        <span>800-555-0147</span>
      </div>
      <div class="contact-item contact-email">
        <svg width="20" height="15" viewBox="0 0 20 15" aria-hidden="true">
          <path d="M0 0h20v15H0z M1.5 1.5v.4L10 8l8.5-6.1v-.4z M1.5 3.7v9.8h17V3.7L10 9.8z" fill-rule="evenodd"/>
        </svg>
        <span>dorian@oakharbor-legal.com</span>
      </div>
      <div class="contact-item contact-web">
        <svg width="20" height="20" viewBox="0 0 24 24" aria-hidden="true" fill="none" stroke="#1f2d5c" stroke-width="2">
          <circle cx="12" cy="12" r="10"/>
          <ellipse cx="12" cy="12" rx="4.5" ry="10"/>
          <path d="M2 12h20"/>
        </svg>
        <span>www.oakharbor-legal.com</span>
      </div>
    </div>
  </div>
</body>
</html>
```